Moss Biscuit Guild - A Monthly Subscription Dog Treats Club - Shopify Website Design

A monthly subscription company. Need a Shopify Website Design and uploaded to fully work with Crane Recurrings.

Please look at these sites for examples as well as the images I enclosed.

https://www.platterwisp.com/
https://www.cometnibbles.com/

Number of Pages Required

1 page

```html
<!DOCTYPE html>
<html lang="en">
<head>
<meta charset="utf-8">
<title>Moss Biscuit Guild — A Monthly Box of Treats and Toys</title>
<link rel="stylesheet" href="https://fonts.googleapis.com/css2?family=Montserrat:wght@400;500;600;700;800&display=swap">
<style>
  :root {
    --red: #db3535;
    --ink: #2b2b2b;
    --white: #ffffff;
    --soft-grey: #f9f9f9;
    --yellow: #f5df6a;
    --yellow-deep: #ecd45f;
    --blue: #7d95e2;
    --pink: #fdd8d8;
    --dark: #383436;
    --tan: #c9a47c;
  }
  * { box-sizing: border-box; margin: 0; padding: 0; }
  html, body { width: 1200px; height: 2574px; overflow: hidden; }
  body {
    font-family: "Montserrat", sans-serif;
    color: var(--ink);
    background: var(--white);
    position: relative;
  }
  .abs { position: absolute; }

  /* header */
  .brand { left: 158px; top: 24px; display: flex; flex-direction: column; align-items: center; gap: 6px; }
  .brand-mark { width: 22px; height: 22px; background: var(--ink); }
  .brand-name { font-size: 12px; font-weight: 600; color: var(--ink); }
  .nav { top: 38px; left: 0; width: 1200px; height: 16px; }
  .nav a { position: absolute; font-size: 11px; font-weight: 600; color: var(--ink); text-decoration: none; }
  .nav a.active { color: var(--red); }
  .cart { left: 1020px; top: 34px; }

  /* hero */
  .hero-title { left: 158px; top: 158px; font-size: 47px; line-height: 45px; font-weight: 700; letter-spacing: 0.5px; width: 500px; }
  .btn {
    position: absolute; height: 37px; width: 150px; border-radius: 19px;
    display: flex; align-items: center; justify-content: center;
    font-size: 11px; font-weight: 700; letter-spacing: 0.3px; text-transform: uppercase;
  }
  .btn-solid { background: var(--red); color: var(--white); }
  .btn-outline { border: 2px solid var(--red); color: var(--red); background: var(--white); }
  .hero-photo { left: 630px; top: 62px; width: 476px; height: 463px; border-radius: 240px 240px 0 0;
    background: radial-gradient(ellipse at 50% 45%, #b8b2ab 0%, #7d7872 45%, #4a4644 80%); }

  /* how it works */
  .how { top: 525px; left: 0; width: 1200px; height: 545px; background: var(--soft-grey); }
  .section-title { position: absolute; left: 0; width: 1200px; text-align: center; font-size: 23px; font-weight: 600; letter-spacing: 0.5px; }
  .step { position: absolute; top: 130px; width: 240px; text-align: center; }
  .step-art { width: 150px; height: 150px; border-radius: 50%; background: var(--red); margin: 0 auto 62px; }
  .step-label { font-size: 15px; font-weight: 600; letter-spacing: 1px; }
  .step-text { font-size: 12px; line-height: 15px; margin-top: 8px; letter-spacing: 0.3px; }

  /* inside the box */
  .inside { top: 1070px; left: 0; width: 1200px; height: 606px; background: var(--yellow); overflow: hidden; }
  .box-photo { left: 365px; top: 145px; width: 475px; height: 295px;
    background: linear-gradient(160deg, #d9bd9b 0%, var(--tan) 50%, #a98560 100%);
    clip-path: polygon(16% 0, 100% 22%, 85% 100%, 0 76%, 2% 43%); }
  .item { position: absolute; width: 160px; }
  .item h3 { font-size: 15px; font-weight: 700; letter-spacing: 0.3px; }
  .item p { font-size: 12px; line-height: 14.5px; letter-spacing: 0.3px; }
  .item.right-align { text-align: right; }
  .arrows { left: 0; top: 0; }

  /* testimonials */
  .served-sub { position: absolute; left: 0; top: 1782px; width: 1124px; text-align: center; font-size: 15px; letter-spacing: 0.4px; }
  .quote-card { position: absolute; top: 1866px; height: 225px; background: var(--blue); color: var(--white); padding: 38px 24px 0; text-align: center; font-size: 12px; line-height: 14.5px; letter-spacing: 0.2px; }
  .quote-card cite { display: block; text-align: right; font-style: normal; font-weight: 700; font-size: 11px; margin-top: 20px; }
  .quote-photo { position: absolute; top: 1837px; width: 225px; height: 282px; background: linear-gradient(180deg, #8a5a36 0%, #d49a5c 45%, #b06a3a 100%); }
  .next { left: 967px; top: 1960px; width: 36px; height: 36px; background: var(--red); display: flex; align-items: center; justify-content: center; }

  /* newsletter */
  .newsletter { top: 2197px; left: 0; width: 1200px; height: 113px; background: var(--pink); }
  .newsletter h2 { position: absolute; left: 268px; top: 42px; font-size: 23px; font-weight: 600; letter-spacing: 0.5px; }
  .email { position: absolute; left: 558px; top: 38px; width: 375px; height: 37px; background: var(--white); border-radius: 19px; font-size: 11px; font-weight: 600; padding-left: 16px; display: flex; align-items: center; }

  /* footer */
  .footer { top: 2310px; left: 0; width: 1200px; height: 264px; background: var(--dark); color: var(--white); }
  .footer-brand { left: 160px; top: 80px; display: flex; flex-direction: column; align-items: center; gap: 10px; }
  .footer-brand .brand-mark { width: 60px; height: 60px; background: var(--white); }
  .footer-brand .brand-name { color: var(--white); font-size: 13px; font-weight: 600; }
  .footer-col { position: absolute; top: 73px; }
  .footer-col h4 { font-size: 12px; font-weight: 700; letter-spacing: 0.4px; margin-bottom: 14px; }
  .footer-col a { display: block; color: var(--white); text-decoration: none; font-size: 13px; line-height: 22.7px; letter-spacing: 0.3px; }
</style>
</head>
<body>

<header>
  <div class="abs brand"><span class="brand-mark"></span><span class="brand-name">Moss Biscuit Guild</span></div>
  <nav class="abs nav">
    <a class="active" style="left:561px">Home</a>
    <a style="left:644px">About</a>
    <a style="left:729px">Subscriptions</a>
    <a style="left:858px">FAQs</a>
    <a style="left:937px">Contact</a>
  </nav>
  <svg class="abs cart" width="24" height="24" viewBox="0 0 24 24" aria-label="Cart">
    <path d="M1 3h4l3 12h12l3-9H7" fill="none" stroke="#2b2b2b" stroke-width="2.4" stroke-linejoin="round"/>
    <circle cx="9.5" cy="20" r="2" fill="#2b2b2b"/><circle cx="18" cy="20" r="2" fill="#2b2b2b"/>
  </svg>
</header>

<section class="hero">
  <div class="abs hero-photo" role="img" aria-label="Photo of a grey scruffy dog holding a bone-shaped biscuit in its mouth"></div>
  <h1 class="abs hero-title">A Monthly Box of Treats and Toys for your Dog</h1>
  <a class="btn btn-solid" style="left:161px;top:323px">Get Started</a>
  <a class="btn btn-outline" style="left:327px;top:324px">Give a Gift</a>
</section>

<section class="abs how">
  <h2 class="section-title" style="top:72px">How it Works</h2>
  <div class="step" style="left:142px">
    <div class="step-art" role="img" aria-label="Illustration of a puppy subscribing on a laptop"></div>
    <div class="step-label">SUBSCRIBE</div>
    <p class="step-text">Choose your plan starting at $20 in just one click away.</p>
  </div>
  <div class="step" style="left:480px">
    <div class="step-art" role="img" aria-label="Illustration of a puppy in a superhero mask delivering a parcel"></div>
    <div class="step-label">SHIP</div>
    <p class="step-text">Free shipping inside United States</p>
  </div>
  <div class="step" style="left:818px">
    <div class="step-art" role="img" aria-label="Illustration of a happy puppy with a bone and food bowl"></div>
    <div class="step-label">ENJOY</div>
    <p class="step-text">Give your dog a month-long treats and toys</p>
  </div>
  <a class="btn btn-solid" style="left:526px;top:433px">See Our Plans</a>
</section>

<section class="abs inside">
  <h2 class="section-title" style="top:72px">What is inside the Box</h2>
  <div class="abs box-photo" role="img" aria-label="Photo of a closed brown cardboard shipping box"></div>
  <svg class="abs arrows" width="1200" height="606" viewBox="0 0 1200 606" fill="none" stroke="#2b2b2b" stroke-width="3" stroke-linecap="round" stroke-linejoin="round">
    <path d="M438 192 C432 170 415 158 393 160"/><path d="M403 150 L393 160 L404 170"/>
    <path d="M820 232 C840 232 858 222 868 206"/><path d="M858 210 L868 206 L870 218"/>
    <path d="M438 356 C436 378 420 390 398 390"/><path d="M408 380 L398 390 L409 398"/>
    <path d="M787 362 C808 352 830 358 838 376"/><path d="M828 370 L838 376 L840 364"/>
  </svg>
  <div class="item right-align" style="left:213px;top:156px"><h3>Puppy Treats</h3><p>Lorem ipsum dolor sit amet, consectetur adipiscing elit.</p></div>
  <div class="item" style="left:872px;top:127px"><h3>Puppy Toys</h3><p>Lorem ipsum dolor sit amet, consectetur adipiscing elit.</p></div>
  <div class="item right-align" style="left:218px;top:382px"><h3>Puppy Toys</h3><p>Lorem ipsum dolor sit amet, consectetur adipiscing elit.</p></div>
  <div class="item" style="left:842px;top:392px"><h3>Puppy Toys</h3><p>Lorem ipsum dolor sit amet, consectetur adipiscing elit.</p></div>
  <a class="btn btn-solid" style="left:526px;top:494px">Get Started</a>
</section>

<section class="testimonials">
  <h2 class="section-title" style="top:1744px;width:1124px">Over 1,000,000 Dogs Served</h2>
  <p class="served-sub">See what are our customers have to say</p>

  <blockquote class="quote-card" style="left:119px;width:225px">“ Lorem ipsum dolor sit amet, consectetur adipiscing elit, sed do eiusmod tempor incididunt ut labore et dolore magna aliqua. maecenas accumsan lacus vel facilisis. ”<cite>Tess Marlow</cite></blockquote>
  <div class="quote-photo" style="left:344px" role="img" aria-label="Photo of a smiling corgi lying on dry dog food"></div>
  <blockquote class="quote-card" style="left:569px;width:225px">“ Lorem ipsum dolor sit amet, consectetur adipiscing elit, sed do eiusmod tempor incididunt ut labore et dolore magna aliqua. maecenas accumsan lacus vel facilisis. ”<cite>Tess Marlow</cite></blockquote>
  <div class="quote-photo" style="left:794px" role="img" aria-label="Photo of a smiling corgi lying on dry dog food"></div>
  <blockquote class="quote-card" style="left:1019px;width:225px">“ Lorem ipsum dolor sit amet, consectetur adipiscing elit, sed do eiusmod tempor incididunt ut labore et dolore magna aliqua. maecenas accumsan lacus vel facilisis. ”<cite>Tess Marlow</cite></blockquote>
  <div class="abs next" aria-label="Next">
    <svg width="20" height="16" viewBox="0 0 20 16" fill="none" stroke="#fff" stroke-width="2" stroke-linecap="round" stroke-linejoin="round"><path d="M2 8h16M12 2l6 6-6 6"/></svg>
  </div>
</section>

<section class="abs newsletter">
  <h2>Join Our Newsletter!</h2>
  <div class="email">Your Email</div>
  <a class="btn btn-solid" style="left:783px;top:38px">Get Started</a>
</section>

<footer class="abs footer">
  <div class="abs footer-brand"><span class="brand-mark"></span><span class="brand-name">Moss Biscuit Guild</span></div>
  <div class="footer-col" style="left:392px"><h4>SERVICES</h4><a>Subscriptions</a><a>Coffee Gifts</a></div>
  <div class="footer-col" style="left:649px"><h4>QUICK LINKS</h4><a>FAQs</a><a>Resources</a><a>Blogs</a></div>
  <div class="footer-col" style="left:908px"><h4>INFORMATION</h4><a>About Us</a><a>Contact Us</a><a>Terms &amp; Coniditions</a><a>Private Privacy</a></div>
</footer>

</body>
</html>
```